A New Website - Harwell & Tansley Trade Council

Website Brief for Harwell and Tansley Trade Council
Overview

The chamber needs to revamp the current website that is not working.
www.harwellandtansleycouncil.example
We are looking to revamp the website and create a new professional, user-friendly, and dynamic website to showcase the chamber's services while allowing minimal day-to-day interference for the in house team.

The Chamber and members use the website for :
1. Presenting the chamber , members, activities and services to the business community.
2. The User will be able to
1. See our activities, events and register interest
2. Access membership information, benefits and register using an external link ( Pellory Mailhub )
3. Access News and reports that our team posts ( either in the website or using an external source)
4. Business will be able to access our members Directory ( in the website or outside throgh links)
5. Include a Chatterlo Chat for easy access to our team with an initial set of automated responses.

The rest of the pages will offer general information about the chamber, our structure and our services .

Target Market(s)

Corporates , Governments & Business Executives

Industry/Entity Type

Chamber of Commerce

Coding

Coded - Design and coding required

Number of Pages Required

5+ page

Font styles to use
Sans Serif
Other font styles liked:
• we are suing georgia in house for all publications

Colors
0054AA
0677BA
7BADD7
CADEEF
E8F1F8
FFF300
FFF600
FEFA6F
FFFEC7
FFFEE8
EB3D1F
EC4F4E
F09395
F8D3D4
FCEDEE

Requirements
Must have
• A clean Design, corporate , with high quality images mainly hours and a few generic ones.
Nice to have
• Responsive, user friendly quick
Should not have
• should not be busy , or chidish..

```html
<!DOCTYPE html>
<html lang="en">
<head>
<meta charset="utf-8">
<title>Harwell &amp; Tansley Trade Council</title>
<link rel="stylesheet" href="https://fonts.googleapis.com/css2?family=Gelasio:wght@400;600;700&display=swap">
<style>
:root{
  --navy:#1b3d8f;
  --brand:#0054AA;
  --band:#2b5e9e;
  --strip:#2460ad;
  --ink:#1d1d1d;
  --muted:#7d92c4;
  --white:#ffffff;
  --footer:#141414;
}
*{margin:0;padding:0;box-sizing:border-box}
html,body{width:1200px;height:4847px;overflow:hidden}
body{position:relative;background:var(--white);font-family:"Gelasio",Georgia,serif;color:var(--ink)}
.abs{position:absolute}
.btn{position:absolute;display:flex;align-items:center;justify-content:center;border-radius:24px;font-size:13px;background:var(--navy);color:var(--white);white-space:nowrap}
.btn.ghost{background:transparent;border:2px solid var(--navy);color:var(--navy)}
.btn.ghost-light{background:transparent;border:1.5px solid var(--white);color:var(--white)}
.photo{position:absolute}
h2{font-weight:700}

.topbar{left:0;top:0;width:1200px;height:38px;background:var(--navy);color:var(--white);font-size:13px}
.topbar .hours{position:absolute;left:757px;top:11px;white-space:nowrap}
.hero{left:0;top:38px;width:1200px;height:564px;background:linear-gradient(180deg,#3c3a3a 0%,#57504a 45%,#2f2c2b 100%)}
.logo-mark{position:absolute;border-radius:50%}
.nav{position:absolute;top:76px;font-size:20px;color:var(--white);white-space:nowrap}
.hero-title{left:0;width:1200px;top:212px;text-align:center;color:var(--white);font-size:48px;font-weight:700}
.hero-sub{left:380px;width:540px;top:282px;text-align:center;color:var(--white);font-size:19px;line-height:22px}
.dot{position:absolute;top:536px;width:11px;height:11px;border-radius:50%;background:var(--white)}

.section-title{font-size:34px;font-weight:700}
.body-text{font-size:14.5px;line-height:20.6px}

.partner{position:absolute;top:1306px;font-size:38px;color:#222;text-align:center;width:200px;white-space:nowrap}

.experts{left:0;top:1448px;width:1200px;height:557px;background:var(--navy)}
.experts .strip{position:absolute;left:0;top:0;width:1200px;height:68px;background:var(--strip)}
.card{position:absolute;top:1516px;width:266px;height:367px;background:var(--white)}
.card .avatar{position:absolute;left:18px;top:24px;width:108px;height:108px;border-radius:50%;background:#b8b8b8}
.card .name{position:absolute;left:29px;top:142px;font-size:13px;font-weight:700;line-height:15px;width:220px}
.card .role{position:absolute;left:29px;top:178px;font-size:12px;color:var(--brand)}
.card .desc{position:absolute;left:29px;top:200px;width:212px;font-size:12px;line-height:15.5px;color:#333}
.card .soc{position:absolute;top:312px;width:18px;height:18px;border:1.8px solid var(--navy);border-radius:4px}
.card .go{position:absolute;left:200px;top:308px}

.stat-num{position:absolute;font-size:48px;color:var(--brand)}
.stat-txt{position:absolute;font-size:21px;line-height:30px;color:var(--white)}

.quote{position:absolute;font-size:19.5px;line-height:26px;color:#222}
.qmark{position:absolute}
.author{position:absolute;font-size:15px;color:#555;white-space:nowrap}
.author b{font-weight:600;color:#444}

.footer{left:0;top:4488px;width:1200px;height:359px;background:var(--footer);color:#cfcfcf}
.footer h4{position:absolute;font-size:15px;font-weight:700;color:var(--white);white-space:nowrap}
.footer li{list-style:none;font-size:12.5px;height:25.6px;color:var(--white);display:flex;align-items:center;white-space:nowrap}
.footer li::before{content:"";width:7px;height:7px;border-radius:50%;background:var(--white);margin-right:12px}
</style>
</head>
<body>

<div class="abs hero photo" role="img" aria-label="Conference panel of business leaders seated at a table with flags behind them"></div>
<div class="abs hero" style="background:rgba(20,24,40,0.35)"></div>
<div class="abs topbar">
  <svg class="abs" style="left:716px;top:6px" width="26" height="26" viewBox="0 0 26 26" fill="none" stroke="#fff" stroke-width="1.6"><circle cx="13" cy="9" r="5"/><path d="M4 23c1-5 5-7 9-7s8 2 9 7"/></svg>
  <span class="hours">Monday - Friday 09:30-17:00. (+44) 207 000 4418</span>
</div>
<div class="logo-mark" style="left:113px;top:47px;width:94px;height:94px;background:#ffffff;border:4px solid var(--navy)"></div>
<div class="abs" style="left:236px;top:62px;width:86px;height:70px;background:rgba(255,255,255,0.25)"></div>
<span class="nav" style="left:441px">Home</span>
<span class="nav" style="left:526px">About us</span>
<span class="nav" style="left:637px">Find support</span>
<span class="nav" style="left:785px">Resources</span>
<span class="nav" style="left:908px">News</span>
<span class="nav" style="left:982px">Contacts us</span>
<div class="abs hero-title">Engage</div>
<div class="abs hero-sub">Joining the H&amp;TTC gives you access to a wide range of business services, from networking events to bespoke advice.</div>
<div class="btn" style="left:455px;top:427px;width:143px;height:43px">Get Started</div>
<div class="btn ghost-light" style="left:617px;top:427px;width:145px;height:43px">See benifits</div>
<div class="dot" style="left:527px;background:var(--brand)"></div>
<div class="dot" style="left:552px"></div>
<div class="dot" style="left:576px"></div>
<div class="dot" style="left:601px"></div>

<h2 class="abs section-title" style="left:111px;top:680px">About us</h2>
<p class="abs body-text" style="left:111px;top:742px;width:450px">The Harwell &amp; Tansley Trade Council stands as a leading international business organisation, uniting members committed to responsible economic and social development, open markets and the principles of the rule of law and democracy. Its membership comprises prominent global companies across a diverse range of sectors, including banking and finance, consulting, consumer goods, energy and mining, manufacturing, media, tourism, technology and infrastructure. Through this broad spectrum of industries, the Chamber fosters a collaborative environment where leaders work towards sustainable growth and mutual prosperity in the UK, Colombia, and Latin America.</p>
<div class="btn" style="left:113px;top:1055px;width:188px;height:45px">Meet Our Members</div>
<div class="btn ghost" style="left:320px;top:1055px;width:120px;height:45px">Time line</div>
<div class="abs" style="left:705px;top:689px;width:381px;height:370px;background:var(--navy);border-radius:14px"></div>
<div class="abs" style="left:705px;top:711px;width:359px;height:348px;background:var(--white);border-radius:0 14px 0 0"></div>
<div class="photo" style="left:653px;top:741px;width:379px;height:371px;border-radius:14px;background:linear-gradient(160deg,#6f7a52 0%,#5b4a3f 50%,#1e1b1a 100%)" role="img" aria-label="Group of women members at a chamber reception"></div>

<h2 class="abs" style="left:0;width:1200px;top:1192px;text-align:center;font-size:32px"><span style="color:var(--brand)">Trusted</span> Partner</h2>
<span class="partner" style="left:0;width:160px;font-size:22px;top:1316px;text-align:left">Norvale business</span>
<span class="partner" style="left:154px">Quillo</span>
<span class="partner" style="left:370px">Brightmere</span>
<span class="partner" style="left:588px;font-size:26px;top:1316px">Ashcombe &amp; Reed</span>
<span class="partner" style="left:805px">Tallow</span>
<span class="partner" style="left:1010px">Vantrel</span>

<div class="abs experts"><div class="strip"></div></div>
<h2 class="abs" style="left:109px;top:1458px;font-size:33px;color:var(--white)">Experts &amp; Leadership</h2>
<p class="abs" style="left:111px;top:1548px;width:355px;font-size:14px;line-height:15.6px;color:var(--muted)">Through this broadspectrum of industries, the Chamber fosters a collaborative environment where leaders work towardssustainable growth and mutual prosperity in both the UK,Colombia and Latin America. Its membership comprises prominent global companies across a diverse range ofsectors, including banking and finance, consulting,consumer goods, energy and mining, manufacturing, media, technology, and infrastructure. Its membership comprises prominent global companies across a diverse range of sectors, including banking and finance, consulting,consumer goods, energy and mining, manufacturing.</p>
<div class="btn" style="left:113px;top:1821px;width:263px;height:45px;background:var(--white);color:var(--navy)">Our Board of Directors &amp; Team</div>

<div class="card" style="left:545px">
  <div class="avatar" role="img" aria-label="Portrait photo of the honorary president"></div>
  <div class="name">Tomas Arvelo<br>Quintanar</div>
  <div class="role">Honorary President</div>
  <div class="desc">Ambassador Extraordinary and Plenipotentiary of the Republic of Colombia to the Government of the United Kingdom of Great Britain and Northern Ireland.</div>
  <div class="soc" style="left:31px"></div><div class="soc" style="left:56px"></div>
  <svg class="go" width="24" height="24" viewBox="0 0 24 24"><circle cx="12" cy="12" r="11" fill="var(--navy)"/><path d="M7 12h9M12.5 8l4 4-4 4" stroke="#fff" stroke-width="2" fill="none"/></svg>
</div>
<div class="card" style="left:822px">
  <div class="avatar" role="img" aria-label="Portrait photo of the honorary president"></div>
  <div class="name">Lord Edwin Harcastle,<br>Baron of Fenwold</div>
  <div class="role">Honorary President</div>
  <div class="desc">Chairman of ClearHorizon Fund, a climate growth equity venture established in partnership with Meridian Growth; Chairman of Leeward Analytics.</div>
  <div class="soc" style="left:31px"></div><div class="soc" style="left:56px"></div>
  <svg class="go" width="24" height="24" viewBox="0 0 24 24"><circle cx="12" cy="12" r="11" fill="var(--navy)"/><path d="M7 12h9M12.5 8l4 4-4 4" stroke="#fff" stroke-width="2" fill="none"/></svg>
</div>

<h2 class="abs" style="left:109px;top:2080px;font-size:30px;line-height:32px">Jobs and Work Experience<br>Opportunities</h2>
<p class="abs body-text" style="left:111px;top:2156px;width:440px;font-size:14px;line-height:17px">The world's largest and most experienced private equity teams, with more than 170 investment professionals across four continents.</p>
<p class="abs body-text" style="left:111px;top:2226px;width:440px;font-size:14px;line-height:17px">Please include your CV and motivation letter stating your area of interest and your availability to start.</p>
<svg class="abs" style="left:109px;top:2305px" width="20" height="16" viewBox="0 0 20 16" fill="none" stroke="var(--navy)" stroke-width="1.6"><rect x="1" y="1" width="18" height="14"/><path d="M1 1l9 8 9-8"/></svg>
<span class="abs" style="left:137px;top:2304px;font-size:13.5px;font-weight:700;color:var(--navy)">info@harwellandtansleycouncil.example</span>
<div class="btn" style="left:113px;top:2380px;width:145px;height:47px">Apply Now</div>
<div class="btn" style="left:277px;top:2380px;width:144px;height:47px">Online form</div>
<div class="photo" style="left:579px;top:2088px;width:508px;height:339px;background:linear-gradient(170deg,#6b5446 0%,#3a2a24 55%,#1c1512 100%)" role="img" aria-label="Young professionals smiling together at an evening networking event"></div>

<div class="abs" style="left:0;top:2526px;width:1200px;height:265px;background:var(--band)"></div>
<h2 class="abs" style="left:0;width:1200px;top:2580px;text-align:center;color:var(--white);font-size:28px">How to Find Us and Opening Times (By appointment only) <span style="color:#c9d6ea;font-weight:400">?</span></h2>
<p class="abs" style="left:330px;width:540px;top:2627px;text-align:center;color:#d7e1f0;font-size:17.5px;line-height:21px">Join us for a cup of coffee and get to know the Chamber, the business lounge and its facilities.</p>
<div class="btn" style="left:514px;top:2701px;width:144px;height:45px;background:var(--strip)">Contact Us</div>

<div class="photo" style="left:111px;top:2884px;width:976px;height:519px;background:linear-gradient(135deg,#2a3350 0%,#1d2440 60%,#161b30 100%)" role="img" aria-label="Exhibition hall with delegates visiting chamber stands"></div>
<h2 class="abs" style="left:150px;top:2928px;font-size:30px;color:var(--white)">Why Join Us ?</h2>
<span class="stat-num" style="left:258px;top:3020px">20</span>
<span class="stat-txt" style="left:335px;top:3036px">Years of trade &amp;<br>Investment support<br>experience</span>
<span class="stat-num" style="left:680px;top:3020px">+17k</span>
<span class="stat-txt" style="left:812px;top:3036px">High profile business<br>and government<br>contacts</span>
<span class="stat-num" style="left:216px;top:3190px">500</span>
<span class="stat-txt" style="left:335px;top:3206px">High Profile Events</span>
<span class="stat-num" style="left:724px;top:3190px">25</span>
<span class="stat-txt" style="left:801px;top:3206px">Missions and Market<br>visits organised</span>
<div class="btn" style="left:523px;top:3300px;width:145px;height:45px;background:var(--strip)">See Benefits</div>

<h2 class="abs" style="left:111px;top:3480px;font-size:31px">Attend our Events</h2>
<p class="abs body-text" style="left:111px;top:3543px;width:490px;font-size:14px">TextDiscover our events programme. Networking is at the heart of what we do. All of our upcoming on-demand events, as well as our partner events, bring together leading figures from politics and business together with experts from our member companies to discuss and propose solutions to prevailing economic, political and trade issues that enhance the relationship between the UK, Colombia and Latin America.</p>
<div class="btn" style="left:113px;top:3771px;width:243px;height:46px">Access our events programme</div>
<div class="abs" style="left:653px;top:3482px;width:453px;height:344px;border-top:5px solid var(--navy);border-right:5px solid var(--navy)"></div>
<div class="photo" style="left:632px;top:3501px;width:453px;height:148px;border:3px solid #fff;background:linear-gradient(120deg,#cfd3d8 0%,#6d655e 60%,#c9b13a 100%)" role="img" aria-label="Speakers at a conference panel"></div>
<div class="photo" style="left:596px;top:3662px;width:245px;height:170px;border:3px solid #fff;background:linear-gradient(160deg,#8c7a66 0%,#3a302a 100%)" role="img" aria-label="Guests at a formal chamber dinner"></div>
<div class="photo" style="left:856px;top:3649px;width:229px;height:147px;border:3px solid #fff;background:linear-gradient(160deg,#4c6079 0%,#1f2530 100%)" role="img" aria-label="Audience listening to a keynote speech"></div>

<div class="abs" style="left:109px;top:3926px;width:978px;height:47px;background:var(--strip)"></div>
<h2 class="abs" style="left:109px;width:978px;top:3932px;text-align:center;color:var(--white);font-size:28px">What our members and clients say about us</h2>
<div class="abs" style="left:109px;top:3973px;width:978px;height:423px;border:5px solid var(--navy);border-top:none"></div>
<div class="abs" style="left:117px;top:3982px;width:466px;height:401px;border:2px solid var(--navy)"></div>
<div class="abs" style="left:594px;top:3982px;width:486px;height:401px;border:2px solid var(--navy)"></div>
<svg class="qmark" style="left:154px;top:4044px" width="70" height="48" viewBox="0 0 70 48"><path d="M0 0h30v24L18 48H6l8-20H0zM38 0h30v24L56 48H44l8-20H38z" fill="#1a1a1a"/></svg>
<svg class="qmark" style="left:619px;top:4044px" width="70" height="48" viewBox="0 0 70 48"><path d="M0 0h30v24L18 48H6l8-20H0zM38 0h30v24L56 48H44l8-20H38z" fill="#1a1a1a"/></svg>
<p class="quote" style="left:212px;top:4098px;width:335px">"The Meet the Buyer Latin America event organised by the Harwell &amp; Tansley Trade Council was by far the best on-line event I have atatended since I have been Export Manager at Orchardley Cider (close to 5 years"</p>
<p class="quote" style="left:694px;top:4080px;width:290px">The conference was not only intellectually stimulating but also impeccably organised, which made the experience all the more enjoyable.</p>
<div class="abs" style="left:161px;top:4286px;width:42px;height:42px;border-radius:50%;background:#c4b3a5" role="img" aria-label="Member portrait"></div>
<div class="author" style="left:224px;top:4286px"><b>Marcus Feld, Orchardley Cider,</b><br><span style="font-size:14px">Meet The Buyer Programme</span></div>
<div class="abs" style="left:644px;top:4286px;width:42px;height:42px;border-radius:50%;background:#a6907f" role="img" aria-label="Member portrait"></div>
<div class="author" style="left:703px;top:4286px"><b>Lucia Ventosa,</b><br><span style="font-size:14px">Conference</span></div>
<svg class="abs" style="left:33px;top:4156px" width="40" height="40" viewBox="0 0 40 40"><circle cx="20" cy="20" r="19" fill="var(--strip)"/><path d="M29 20H12M18 13l-7 7 7 7" stroke="#fff" stroke-width="2.4" fill="none"/></svg>
<svg class="abs" style="left:1122px;top:4156px" width="40" height="40" viewBox="0 0 40 40"><circle cx="20" cy="20" r="19" fill="var(--strip)"/><path d="M11 20h17M22 13l7 7-7 7" stroke="#fff" stroke-width="2.4" fill="none"/></svg>

<div class="abs footer">
  <div class="logo-mark" style="left:117px;top:53px;width:116px;height:116px;border:3px solid #fff"></div>
  <p class="abs" style="left:117px;top:182px;width:320px;font-size:10.5px;line-height:11.5px;color:#a8a8a8">The Harwell &amp; Tansley Trade Council stands as a leading international business organisation, uniting members committed to responsible economic and social development, open markets and the principles of the rule of law and democracy</p>
  <h4 style="left:511px;top:74px">Popular Services</h4>
  <ul class="abs" style="left:507px;top:105px">
    <li>Membership Benefits</li>
    <li>Membership Directory</li>
    <li>Our Board</li>
    <li>Events</li>
    <li>Business Visits &amp; Market Support</li>
    <li>Campaigns</li>
    <li>Brand Opportunities</li>
  </ul>
  <h4 style="left:751px;top:70px">Connect with H&amp;TTC</h4>
  <svg class="abs" style="left:753px;top:108px" width="20" height="20" viewBox="0 0 20 20" fill="none" stroke="#fff" stroke-width="1.5"><path d="M4 2l3 1 1 4-2 1.5c1 2.5 3 4.5 5.5 5.5L13 12l4 1 1 3-2 2C9 18 2 11 2 4z"/></svg>
  <span class="abs" style="left:785px;top:109px;font-size:14px;color:#fff;white-space:nowrap">+44(0) 207 000 4418</span>
  <svg class="abs" style="left:754px;top:143px" width="20" height="15" viewBox="0 0 20 15" fill="none" stroke="#fff" stroke-width="1.5"><rect x="1" y="1" width="18" height="13"/><path d="M1 1l9 7 9-7"/></svg>
  <span class="abs" style="left:792px;top:141px;font-size:14px;color:#fff;white-space:nowrap">info@harwellandtansleycouncil.example</span>
  <span class="abs" style="left:115px;top:325px;font-size:11px;color:#bdbdbd;white-space:nowrap">Copyrights©2025, Harwell Tansley Trade Council</span>
  <div class="abs" style="left:971px;top:322px;width:22px;height:22px;border-radius:50%;background:#8a8a8a"></div>
  <div class="abs" style="left:1001px;top:322px;width:22px;height:22px;border-radius:50%;background:#8a8a8a"></div>
  <div class="abs" style="left:1031px;top:322px;width:22px;height:22px;border-radius:50%;background:#8a8a8a"></div>
  <div class="abs" style="left:1061px;top:322px;width:22px;height:22px;border-radius:50%;background:#8a8a8a"></div>
</div>

</body>
</html>
```